Pomvel stationary merch

We are going to sell a collection of notebooks of different styles but under same theme. Our theme is inspired by the planets of space in pastel colors. For example, one notebook of the collection is based on Planet Earth so that it is is pastel green color with a minimalistic sketch of planet Earth.

```html
<!DOCTYPE html>
<html lang="en">
<head>
<meta charset="UTF-8">
<title>Planet Notebooks Collection</title>
<link href="https://fonts.googleapis.com/css2?family=Open+Sans:wght@300;400&display=swap" rel="stylesheet">
<style>
  :root {
    --bg: #ffffff;
    --lavender: #a3a6f5;
    --periwinkle: #9ea8f2;
    --lilac: #c3a5f0;
    --pink: #f4b3dd;
    --blush: #f7c7e6;
    --sky: #a6d6f5;
    --aqua: #a9e4f3;
    --rule: #5b4fe6;
    --title: #7b7fe9;
    --earth-sea: #8fd3f2;
    --earth-land: #d7ee86;
    --planet-pink: #e27ac8;
    --planet-light: #f3b8e4;
  }
  * { margin: 0; padding: 0; box-sizing: border-box; }
  html, body { width: 1200px; height: 1200px; overflow: hidden; background: var(--bg); }
  .canvas { position: relative; width: 1200px; height: 1200px; }

  .sheet { position: absolute; overflow: hidden; }

  .earth-theme {
    background:
      radial-gradient(ellipse at 20% 75%, rgba(255,255,255,0.45), transparent 45%),
      linear-gradient(180deg, var(--lavender) 0%, var(--periwinkle) 35%, var(--lilac) 65%, var(--pink) 88%, var(--blush) 100%);
  }
  .planet-theme {
    background:
      radial-gradient(ellipse at 30% 70%, rgba(255,255,255,0.4), transparent 40%),
      linear-gradient(180deg, var(--lavender) 0%, var(--periwinkle) 30%, var(--sky) 70%, var(--aqua) 100%);
  }

  .cover-earth { left: 285px; top: 144px; width: 223px; height: 444px; }
  .page-earth { left: 569px; top: 145px; width: 284px; height: 402px; }
  .page-pink { left: 389px; top: 631px; width: 316px; height: 447px; }
  .cover-pink { left: 806px; top: 625px; width: 219px; height: 456px; }

  .planet { position: absolute; border-radius: 50%; }
  .planet-earth {
    background: radial-gradient(circle at 40% 40%, var(--earth-land) 0%, var(--earth-sea) 45%, #7cc7ee 100%);
  }
  .planet-rose {
    background: radial-gradient(circle at 50% 40%, var(--planet-light) 0%, #ec9ad6 50%, var(--planet-pink) 100%);
  }
  .cover-earth .planet { left: 44px; top: 125px; width: 156px; height: 156px; }
  .page-earth .planet { left: 46px; top: 106px; width: 182px; height: 182px; }
  .page-pink .planet { left: 55px; top: 119px; width: 206px; height: 206px; }
  .cover-pink .planet { left: 36px; top: 146px; width: 152px; height: 152px; }

  .rules { position: absolute; left: 0; top: 0; }

  .cover-title {
    position: absolute;
    right: 12px;
    bottom: 54px;
    font-family: "Open Sans", sans-serif;
    font-weight: 300;
    font-size: 25px;
    letter-spacing: -0.5px;
    color: var(--title);
  }
  .cover-pink .cover-title { bottom: 52px; }
</style>
</head>
<body>
<main class="canvas">

  <section class="sheet cover-earth earth-theme">
    <div class="planet planet-earth" role="img" aria-label="Watercolour sketch of planet Earth in pastel green and blue"></div>
    <p class="cover-title">NOTEBOOK</p>
  </section>

  <section class="sheet page-earth earth-theme">
    <div class="planet planet-earth" role="img" aria-label="Watercolour sketch of planet Earth in pastel green and blue"></div>
    <svg class="rules" width="284" height="402" viewBox="0 0 284 402">
      <g stroke="var(--rule)" stroke-width="0.8">
        <line x1="21" x2="262" y1="39" y2="39"/><line x1="21" x2="262" y1="60.6" y2="60.6"/>
        <line x1="21" x2="262" y1="82.2" y2="82.2"/><line x1="21" x2="262" y1="103.8" y2="103.8"/>
        <line x1="21" x2="262" y1="125.4" y2="125.4"/><line x1="21" x2="262" y1="147" y2="147"/>
        <line x1="21" x2="262" y1="168.6" y2="168.6"/><line x1="21" x2="262" y1="190.2" y2="190.2"/>
        <line x1="21" x2="262" y1="211.8" y2="211.8"/><line x1="21" x2="262" y1="233.4" y2="233.4"/>
        <line x1="21" x2="262" y1="255" y2="255"/><line x1="21" x2="262" y1="276.6" y2="276.6"/>
        <line x1="21" x2="262" y1="298.2" y2="298.2"/><line x1="21" x2="262" y1="319.8" y2="319.8"/>
        <line x1="21" x2="262" y1="341.4" y2="341.4"/><line x1="21" x2="262" y1="363" y2="363"/>
      </g>
    </svg>
  </section>

  <section class="sheet page-pink planet-theme">
    <div class="planet planet-rose" role="img" aria-label="Watercolour sketch of a pink cratered planet"></div>
    <svg class="rules" width="316" height="447" viewBox="0 0 316 447">
      <g stroke="var(--rule)" stroke-width="0.8">
        <line x1="24" x2="292" y1="44" y2="44"/><line x1="24" x2="292" y1="67.8" y2="67.8"/>
        <line x1="24" x2="292" y1="91.6" y2="91.6"/><line x1="24" x2="292" y1="115.4" y2="115.4"/>
        <line x1="24" x2="292" y1="139.2" y2="139.2"/><line x1="24" x2="292" y1="163" y2="163"/>
        <line x1="24" x2="292" y1="186.8" y2="186.8"/><line x1="24" x2="292" y1="210.6" y2="210.6"/>
        <line x1="24" x2="292" y1="234.4" y2="234.4"/><line x1="24" x2="292" y1="258.2" y2="258.2"/>
        <line x1="24" x2="292" y1="282" y2="282"/><line x1="24" x2="292" y1="305.8" y2="305.8"/>
        <line x1="24" x2="292" y1="329.6" y2="329.6"/><line x1="24" x2="292" y1="353.4" y2="353.4"/>
        <line x1="24" x2="292" y1="377.2" y2="377.2"/><line x1="24" x2="292" y1="401" y2="401"/>
      </g>
    </svg>
  </section>

  <section class="sheet cover-pink planet-theme">
    <div class="planet planet-rose" role="img" aria-label="Watercolour sketch of a pink cratered planet"></div>
    <p class="cover-title">NOTEBOOK</p>
  </section>

</main>
</body>
</html>
```